Motorcycle Shop Business Card

New business card for Motorcycle repair and customization shop.Business name: Copper Falcon Chris Morris443-865-5190, 7214 Quarry Lane Arbutus, MD 21227. www.dale@copperfalconcustoms.example. I uploaded some motorcycle images and logo and a couple of our calendar shoots. They do not have to be used on card just examples of some of our work and past graphic work.
We work on Vantor Brennick and Custom Built Motorcycles.

Looking for front and back design

Target Market(s)

Motorcycle owners

Industry/Entity Type

Motorcycle Part

```html
<!DOCTYPE html>
<html lang="en">
<head>
<meta charset="utf-8">
<title>Copper Falcon Business Card</title>
<link rel="stylesheet" href="https://fonts.googleapis.com/css2?family=Bebas+Neue&family=Oswald:wght@500&display=swap">
<style>
  :root {
    --page-bg: #e4e4e4;
    --card-white: #ffffff;
    --ray-grey: #ececec;
    --band-grey: #4b4a4c;
    --ink-dark: #4b4a4c;
    --ink-light: #ffffff;
  }
  * { margin: 0; padding: 0; box-sizing: border-box; }
  html, body {
    width: 1200px;
    height: 967px;
    overflow: hidden;
    background: var(--page-bg);
  }
  .business-card {
    position: absolute;
    left: 100px;
    top: 198px;
    width: 1000px;
    height: 571px;
    background: var(--card-white);
    overflow: hidden;
    box-shadow: 0 10px 30px rgba(0,0,0,0.18);
  }
  .sunburst-backdrop {
    position: absolute;
    inset: 0;
    background: radial-gradient(ellipse at 50% 35%, var(--card-white) 0%, var(--ray-grey) 70%, #f4f4f4 100%);
  }
  .band-rule {
    position: absolute;
    left: 0;
    right: 0;
    height: 4px;
    background: var(--band-grey);
  }
  .band-rule.upper { top: 262px; }
  .info-band {
    position: absolute;
    left: 0;
    right: 0;
    top: 276px;
    height: 218px;
    background: var(--band-grey);
  }
  .band-rule.lower { top: 508px; }
  .brand-block {
    position: absolute;
    left: 0;
    right: 0;
    top: 34px;
    text-align: center;
  }
  .brand-name {
    font-family: "Bebas Neue", sans-serif;
    font-weight: 400;
    font-size: 112px;
    letter-spacing: 8px;
    line-height: 1;
    color: var(--ink-dark);
  }
  .owner-name {
    margin-top: 40px;
    font-family: "Oswald", sans-serif;
    font-weight: 500;
    font-size: 36px;
    letter-spacing: 1px;
    line-height: 1;
    text-transform: uppercase;
    color: var(--ink-dark);
  }
  .motorcycle-art {
    position: absolute;
    left: 395px;
    top: 292px;
    width: 210px;
    height: 186px;
    border-radius: 12px;
    background: linear-gradient(160deg, #f2f2f2, #cfcfcf);
  }
  .contact {
    position: absolute;
    display: flex;
    font-family: "Oswald", sans-serif;
    font-weight: 500;
    color: var(--ink-light);
    font-style: normal;
  }
  .contact svg { flex: none; }
  .contact-phone {
    left: 60px;
    top: 412px;
    align-items: center;
    gap: 14px;
    font-size: 32px;
    line-height: 1;
  }
  .contact-address {
    right: 60px;
    top: 298px;
    flex-direction: column;
    align-items: center;
    gap: 10px;
    font-size: 26px;
    line-height: 1.15;
    text-align: center;
    text-transform: uppercase;
  }
</style>
</head>
<body>
  <article class="business-card">
    <div class="sunburst-backdrop" role="img" aria-label="Light grey sunburst rays radiating behind the shop name"></div>

    <div class="band-rule upper"></div>
    <div class="info-band"></div>
    <div class="band-rule lower"></div>

    <header class="brand-block">
      <h1 class="brand-name">COPPER FALCON</h1>
      <p class="owner-name">Dale Fenwick</p>
    </header>

    <div class="motorcycle-art" role="img" aria-label="Black and white illustration of a custom chopper motorcycle"></div>

    <div class="contact contact-phone">
      <svg width="32" height="32" viewBox="0 0 34 34" aria-hidden="true">
        <circle cx="17" cy="17" r="17" fill="#ffffff"/>
        <path d="M12 9.5c1-.6 2 .2 2.5 1.3l1 2.2c.3.8 0 1.5-.6 2l-1 .8c.8 1.8 2.3 3.3 4.1 4.1l.8-1c.5-.6 1.2-.9 2-.6l2.2 1c1.1.5 1.9 1.5 1.3 2.5-.9 1.6-2.6 2.4-4.4 1.9-4.2-1.2-7.5-4.5-8.7-8.7-.5-1.8.3-3.5 1.8-4.5z" fill="#4b4a4c"/>
      </svg>
      <span>410-555-0137</span>
    </div>

    <address class="contact contact-address">
      <svg width="32" height="32" viewBox="0 0 34 34" aria-hidden="true">
        <circle cx="17" cy="17" r="17" fill="#ffffff"/>
        <path d="M17 7c-3.9 0-7 3-7 6.8 0 5 7 13.2 7 13.2s7-8.2 7-13.2C24 10 20.9 7 17 7zm0 9.5a2.7 2.7 0 1 1 0-5.4 2.7 2.7 0 0 1 0 5.4z" fill="#4b4a4c"/>
      </svg>
      <span>7214 Quarry Lane Elmridge<br>MD 20964</span>
    </address>
  </article>
</body>
</html>
```